Business Card Design For A Renovation Contractor Company

We need a business card for a new company based in Singapore, our company name is "KT Planora". We are a renovation contractor that builds designs into reality. We build more of F&B restaurants, retail stores and commercial offices. We work very closely with designers. The final design should communicate to our client that we are a company that you can trust, that will plan and complete your project without giving you a headache. I like my client to remember my company as "KT". The beauty of SIMPLE is important.

Industry/Entity Type

Contractor

Requirements
Nice to have
• Black or Red base

```html
<!DOCTYPE html>
<html lang="en">
<head>
<meta charset="utf-8">
<title>KT Planora – Business Card</title>
<link rel="stylesheet" href="https://fonts.googleapis.com/css2?family=Questrial&family=Michroma&family=Tinos:wght@700&display=swap">
<style>
  :root {
    --stage: #000000;
    --card: #ffffff;
    --brand-red: #d42b25;
    --ink: #222222;
    --sky-light: #f4f8fb;
    --sky-mid: #d6e5ef;
    --wave-light: #3aa6e0;
    --wave-deep: #1d5cab;
    --wave-night: #1c1f58;
  }
  html, body {
    margin: 0;
    padding: 0;
    width: 1200px;
    height: 960px;
    overflow: hidden;
    background: var(--stage);
  }
  .card {
    position: absolute;
    left: 236px;
    top: 256px;
    width: 730px;
    height: 445px;
    background: var(--card);
    overflow: hidden;
  }
  .card__art {
    position: absolute;
    inset: 0;
  }
  .brand {
    position: absolute;
    left: 48px;
    top: 36px;
    display: flex;
    align-items: center;
    gap: 18px;
  }
  .brand__dot {
    width: 122px;
    height: 122px;
    border-radius: 50%;
    background: var(--brand-red);
    flex: none;
  }
  .brand__text {
    display: flex;
    flex-direction: column;
    padding-top: 8px;
  }
  .brand__name {
    font-family: "Questrial", sans-serif;
    font-size: 62px;
    line-height: 1;
    color: var(--brand-red);
    border-bottom: 2px solid var(--ink);
    padding-bottom: 4px;
    white-space: nowrap;
  }
  .brand__tagline {
    font-family: "Questrial", sans-serif;
    font-size: 22px;
    color: var(--ink);
    margin-top: 2px;
    letter-spacing: 0.3px;
    white-space: nowrap;
  }
  .contact {
    position: absolute;
    left: 0;
    width: 730px;
    text-align: center;
  }
  .contact__name {
    top: 185px;
    left: -10px;
    font-family: "Tinos", serif;
    font-weight: 700;
    font-size: 38px;
    color: var(--brand-red);
  }
  .contact__address {
    top: 272px;
    left: 8px;
    font-family: "Michroma", sans-serif;
    font-style: normal;
    font-size: 15.5px;
    line-height: 22px;
    color: var(--ink);
  }
  .contact__email {
    top: 344px;
    left: -8px;
    font-family: "Tinos", serif;
    font-weight: 700;
    font-size: 26px;
    color: var(--brand-red);
    transform: rotate(-5deg);
  }
</style>
</head>
<body>
  <main class="card">
    <svg class="card__art" width="730" height="445" viewBox="0 0 730 445">
      <defs>
        <linearGradient id="skyFade" x1="0" y1="0" x2="0" y2="1">
          <stop offset="0" stop-color="var(--card)"/>
          <stop offset="0.2" stop-color="var(--sky-light)"/>
          <stop offset="0.75" stop-color="var(--sky-mid)"/>
          <stop offset="1" stop-color="var(--sky-mid)"/>
        </linearGradient>
        <linearGradient id="waveDeep" x1="0" y1="0" x2="0" y2="1">
          <stop offset="0" stop-color="var(--wave-deep)"/>
          <stop offset="1" stop-color="var(--wave-night)"/>
        </linearGradient>
      </defs>
      <rect class="skyline" role="img" aria-label="Faint city skyline of office towers" x="0" y="0" width="730" height="445" fill="url(#skyFade)"/>
      <path class="wave wave--light" d="M0,250 Q365,560 730,258 L730,445 L0,445 Z" fill="var(--wave-light)"/>
      <path class="wave wave--white" d="M0,258 Q365,570 730,266 L730,445 L0,445 Z" fill="var(--card)"/>
      <path class="wave wave--deep" d="M0,266 Q365,580 730,274 L730,445 L0,445 Z" fill="url(#waveDeep)"/>
    </svg>

    <header class="brand">
      <div class="brand__dot"></div>
      <div class="brand__text">
        <div class="brand__name">KT Planora</div>
        <div class="brand__tagline">plans made solid, built right</div>
      </div>
    </header>

    <div class="contact contact__name">Marcus Tan</div>
    <address class="contact contact__address">
      Address:8 Keppel Lane<br>
      #04-1208 Keppel Trade Hub<br>
      Singapore 098765
    </address>
    <div class="contact contact__email">Email: marcus@ktplanora.com</div>
  </main>
</body>
</html>
```